Label for Dog Nourishing CBD Balm

Dear Designers,

We are looking for a packaging expert to design our new Hydrating Balm for dogs which contain a relaxing hemp extract (CBD). The product is intended to be massaged on the dog’s paws to make them softer and promote the animal’s well-being :)

Our company is already selling various relaxing cat & dog products, and we would like this new design to reflect the same "style & feeling" as our current products (see attached ZIP file).

Technical aspects:
- The packaging is a 40ml aluminium jar (58mm x 23mm).
- We are looking to design 2 separate labels (one for the front, one for the back)
- The label dimensions should be : 50mm x 50mm
- Please follow technical guidelines from printer (see ZIP file).

Design aspects:
- The design should be compatible with our brand identity (i.e. fluffly, pure, relaxing, positive, clean & natural).
- People should understand what the product "is" and what the product "does" simply from looking at the design.
- The actual balm is white/yellow in color.
- Soft/rounded shapes are preferred.
- Please use our brand's colors (see typo & colors in ZIP file)
- Please use our brand's fonts (see typo & colors in ZIP file)
- Please use our company logo (see ZIP file).
- The design also needs to convey a strong sense of professionalism as we are an animal "healthcare" brand.
- If you want to include a dog picture, we would prefer you to use a picture of our official brand ambassador (see ZIP file).
- Only original work (no plagiarism will be accepted).

Please don't hesitate to send us a message if you have any questions about the brand, the product or the design requirements.

We look forward to seeing your designs & working on this together !

Thanks & regards,
Marcus

Target Market(s)

Dog owners

Font styles to use
Other font styles liked:
• See ZIP file

Requirements
Must have
• Brand fonts (see typo & colors in ZIP file)
Brand colors (see typo & colors in ZIP file)

```html
<!DOCTYPE html>
<html lang="en">
<head>
<meta charset="utf-8">
<title>Verdalia Soothing Balm – Lid Labels</title>
<link rel="stylesheet" href="https://fonts.googleapis.com/css2?family=Arvo:wght@400&family=Montserrat:wght@500;600;700;800&family=Raleway:wght@400;500&display=swap">
<style>
  :root {
    --green: #3a9a7e;
    --green-deep: #2f8a70;
    --green-soft: #4aa98c;
    --ink: #333333;
    --brand-ink: #1c3a24;
    --paper: #ffffff;
    --backdrop: #ffffff;
  }
  html, body {
    margin: 0;
    padding: 0;
    width: 1200px;
    height: 658px;
    overflow: hidden;
    background: var(--backdrop);
  }
  .canvas {
    position: relative;
    width: 1200px;
    height: 658px;
  }
  .label {
    position: absolute;
    top: 93px;
    width: 480px;
    height: 480px;
  }
  .label--front { left: 100px; }
  .label--back { left: 628px; }

  .label-disc { fill: var(--paper); stroke: #e6e6e6; stroke-width: 1; }
  .label-ring { fill: none; stroke: var(--green); stroke-width: 2.2; }
  .band-line, .band-fill { fill: var(--green); }

  .brand-name {
    font-family: "Arvo", Georgia, serif;
    font-weight: 400;
    fill: var(--brand-ink);
    text-anchor: middle;
  }
  .brand-dot { fill: none; stroke: var(--green); stroke-width: 2.2; }

  .product-title {
    font-family: "Montserrat", Arial, sans-serif;
    font-weight: 800;
    font-size: 53px;
    letter-spacing: -2px;
    fill: var(--ink);
    text-anchor: middle;
  }
  .product-type {
    font-family: "Montserrat", Arial, sans-serif;
    font-weight: 600;
    font-size: 21px;
    letter-spacing: 6px;
    fill: var(--green);
    text-anchor: middle;
  }
  .pack-facts {
    font-family: "Montserrat", Arial, sans-serif;
    font-weight: 600;
    font-size: 14px;
    fill: var(--paper);
    text-anchor: middle;
  }
  .benefit-arc {
    font-family: "Montserrat", Arial, sans-serif;
    font-weight: 500;
    font-size: 19px;
    letter-spacing: 1px;
    fill: var(--paper);
  }
  .section-heading {
    font-family: "Montserrat", Arial, sans-serif;
    font-weight: 700;
    font-size: 14.5px;
    fill: var(--green);
    text-anchor: middle;
  }
  .section-body {
    font-family: "Raleway", Arial, sans-serif;
    font-weight: 500;
    font-size: 11.2px;
    fill: var(--ink);
    text-anchor: middle;
  }
  .distributor {
    font-family: "Montserrat", Arial, sans-serif;
    font-weight: 500;
    font-size: 13px;
    fill: var(--paper);
    text-anchor: middle;
  }
  .distributor--lead { font-weight: 700; }
</style>
</head>
<body>
<main class="canvas">

  <!-- Front label -->
  <svg class="label label--front" viewBox="0 0 480 480" aria-label="Front label">
    <defs>
      <clipPath id="front-disc-clip"><circle cx="240" cy="240" r="232"/></clipPath>
      <linearGradient id="dog-tone" x1="0" y1="0" x2="0" y2="1">
        <stop offset="0" stop-color="#3f9a80"/>
        <stop offset="1" stop-color="#2f8a70"/>
      </linearGradient>
      <path id="front-benefit-path" d="M 35 240 A 205 205 0 0 0 445 240"/>
    </defs>

    <circle class="label-disc" cx="240" cy="240" r="232"/>
    <circle class="label-ring" cx="240" cy="240" r="206"/>

    <circle class="brand-dot" cx="240" cy="92" r="14"/>
    <text class="brand-name" x="240" y="150" font-size="38">VERDALIA</text>

    <text class="product-title" x="240" y="224">SOOTHING</text>
    <text class="product-title" x="240" y="278">BALM</text>
    <text class="product-type" x="243" y="314">CBD BALM</text>

    <g role="img" aria-label="Seated dog silhouette facing right">
      <rect x="62" y="238" width="74" height="92" rx="26" fill="url(#dog-tone)"/>
    </g>
    <g role="img" aria-label="Seated dog silhouette facing left">
      <rect x="344" y="238" width="74" height="92" rx="26" fill="url(#dog-tone)"/>
    </g>

    <g clip-path="url(#front-disc-clip)">
      <rect class="band-line" x="0" y="329" width="480" height="7"/>
      <path class="band-fill" d="M 0 341 H 205 Q 235 341 240 371 Q 245 341 275 341 H 480 V 480 H 0 Z"/>
    </g>

    <text class="pack-facts" x="240" y="390">40g  |  CBD 250mg</text>
    <text class="pack-facts" x="240" y="409">0% THC</text>

    <text class="benefit-arc">
      <textPath href="#front-benefit-path" startOffset="50%" text-anchor="middle">REPAIR  /  NOURISH  /  PROTECT</textPath>
    </text>
  </svg>

  <!-- Back label -->
  <svg class="label label--back" viewBox="0 0 480 480" aria-label="Back label">
    <defs>
      <clipPath id="back-disc-clip"><circle cx="240" cy="240" r="232"/></clipPath>
    </defs>

    <circle class="label-disc" cx="240" cy="240" r="232"/>
    <circle class="label-ring" cx="240" cy="240" r="206"/>

    <circle class="brand-dot" cx="240" cy="68" r="10"/>
    <text class="brand-name" x="240" y="104" font-size="22">VERDALIA</text>

    <text class="section-heading" x="240" y="142">EVERYDAY RELAXATION</text>
    <text class="section-body" x="240" y="158">This balm repairs, nourishes and protects your dog's sensitive</text>
    <text class="section-body" x="240" y="173">skin. Its trusted multi-action formula brings relief to fragile areas</text>
    <text class="section-body" x="240" y="188">and soothes temporary irritations (paw pads, elbows, etc.)</text>

    <text class="section-heading" x="240" y="221">RECOMMENDED USE:</text>
    <text class="section-body" x="240" y="237">Rub a small amount of balm in the palm of your hand and apply to</text>
    <text class="section-body" x="240" y="252">sensitive areas as a daily care ritual. Repeat until the product has</text>
    <text class="section-body" x="240" y="267">been completely absorbed.</text>

    <text class="section-heading" x="240" y="299">INGREDIENTS:</text>
    <text class="section-body" x="240" y="315">Shea Butter, Beeswax, Coconut Oil, Hemp Extract (0% THC).</text>

    <g clip-path="url(#back-disc-clip)">
      <rect class="band-line" x="0" y="329" width="480" height="7"/>
      <path class="band-fill" d="M 0 341 H 205 Q 235 341 240 371 Q 245 341 275 341 H 480 V 480 H 0 Z"/>
    </g>

    <text class="distributor distributor--lead" x="240" y="395">Distributed by: VERDA TRADE KFT.</text>
    <text class="distributor" x="240" y="414">Fenyő utca 14, 1071 Budapest</text>
    <text class="distributor" x="240" y="433">Hungary</text>
  </svg>

</main>
</body>
</html>
```